Construction Company Cellar Horizon needs Business Card

I would like modern looking business card design. I am attaching logo of our company. Please include cell nr 302.481.7736 , email address cellarhorizon4u@mailvex.com, web : cellarhorizon4u.com, please also include wording: Specializing in finishing and remodeling basements. You can play with dark grey and orange colors or any ideas are welcome. Also include social media icons Chatterloop and NestFinder.

```html
<!DOCTYPE html>
<html lang="en">
<head>
<meta charset="utf-8">
<title>Cellar Horizon – Business Card</title>
<link href="https://fonts.googleapis.com/css2?family=Exo+2:wght@400;500;700&display=swap" rel="stylesheet">
<style>
  :root {
    --backdrop: #505050;
    --card: #161616;
    --card-front: #1b1b1b;
    --orange: #f0572a;
    --white: #f4f4f4;
    --social-tile: #111111;
    --social-edge: #2a2a2a;
    --social-text: #9a9a9a;
  }
  html, body {
    margin: 0;
    width: 1200px;
    height: 1000px;
    overflow: hidden;
    background: radial-gradient(ellipse at center, #5a5a5a 0%, var(--backdrop) 70%, #474747 100%);
    font-family: "Exo 2", sans-serif;
  }
  .card {
    position: absolute;
    left: 262px;
    width: 676px;
    height: 406px;
    box-shadow: 0 6px 18px rgba(0,0,0,0.45);
    overflow: hidden;
  }
  .card--front { top: 82px; background: var(--card-front); }
  .card--back { top: 517px; background: var(--card); }

  .texture {
    position: absolute;
    inset: 0;
    background: linear-gradient(135deg, #1e1e1e 0%, #181818 50%, #1d1d1d 100%);
  }

  .lockup {
    position: absolute;
    display: flex;
    flex-direction: column;
    align-items: flex-end;
  }
  .card--front .lockup {
    left: 50%;
    top: 196px;
    transform: translateX(-50%);
  }
  .card--back .lockup {
    left: 36px;
    top: 102px;
  }
  .brand {
    margin: 0;
    color: var(--orange);
    font-weight: 700;
    text-transform: uppercase;
    letter-spacing: 2px;
    white-space: nowrap;
    line-height: 1;
  }
  .card--front .brand { font-size: 54px; }
  .card--back .brand { font-size: 40px; }
  .tagline {
    margin: 8px 0 0;
    color: var(--white);
    font-weight: 400;
    white-space: nowrap;
    letter-spacing: 0.5px;
  }
  .card--front .tagline { font-size: 16px; }
  .card--back .tagline { font-size: 13px; margin-top: 6px; }

  .person {
    position: absolute;
    right: 38px;
    top: 68px;
    text-align: right;
    text-transform: uppercase;
  }
  .person__name { color: var(--white); font-size: 23px; font-weight: 500; line-height: 1; }
  .person__role { color: var(--orange); font-size: 16px; letter-spacing: 2px; margin-top: 4px; }

  .contacts {
    position: absolute;
    left: 36px;
    top: 288px;
    margin: 0; padding: 0;
    list-style: none;
  }
  .contacts li {
    display: flex;
    align-items: center;
    height: 29.5px;
    color: var(--white);
    font-size: 17px;
  }
  .contacts svg { width: 20px; height: 20px; margin-right: 12px; flex: none; }

  .social {
    position: absolute;
    right: 38px;
    top: 306px;
    margin: 0; padding: 0;
    list-style: none;
  }
  .social li {
    display: flex;
    align-items: center;
    justify-content: flex-end;
    height: 36px;
    color: var(--social-text);
    font-size: 15px;
    font-weight: 500;
  }
  .social__tile {
    width: 26px;
    height: 26px;
    margin-right: 10px;
    border-radius: 3px;
    background: var(--social-tile);
    box-shadow: inset 0 1px 2px rgba(0,0,0,0.8), 0 1px 0 var(--social-edge);
  }
</style>
</head>
<body>

<section class="card card--front">
  <div class="texture" role="img" aria-label="Fine diagonal pinstripe texture across the dark card"></div>
  <div class="lockup">
    <h1 class="brand">Cellar Horizon</h1>
    <p class="tagline">Specializing in finishing and remodeling basements</p>
  </div>
</section>

<section class="card card--back">
  <div class="lockup">
    <h2 class="brand">Cellar Horizon</h2>
    <p class="tagline">Specializing in finishing and remodeling basements</p>
  </div>

  <div class="person">
    <div class="person__name">Alex Marlow</div>
    <div class="person__role">Owner</div>
  </div>

  <ul class="contacts">
    <li>
      <svg viewBox="0 0 20 20" aria-hidden="true">
        <rect width="20" height="20" rx="3" fill="var(--orange)"/>
        <rect x="6" y="3.5" width="8" height="13" rx="1.5" fill="none" stroke="var(--card)" stroke-width="1.6"/>
        <circle cx="10" cy="14" r="0.9" fill="var(--card)"/>
      </svg>
      302.481.7736
    </li>
    <li>
      <svg viewBox="0 0 20 20" aria-hidden="true">
        <rect width="20" height="20" rx="3" fill="var(--orange)"/>
        <rect x="4" y="6" width="12" height="8.5" fill="none" stroke="var(--card)" stroke-width="1.5"/>
        <path d="M4 6 L10 11 L16 6" fill="none" stroke="var(--card)" stroke-width="1.5"/>
      </svg>
      cellarhorizon4u@mailvex.com
    </li>
    <li>
      <svg viewBox="0 0 20 20" aria-hidden="true">
        <rect width="20" height="20" rx="3" fill="var(--orange)"/>
        <circle cx="10" cy="10" r="6" fill="none" stroke="var(--card)" stroke-width="1.5"/>
        <ellipse cx="10" cy="10" rx="2.6" ry="6" fill="none" stroke="var(--card)" stroke-width="1.2"/>
        <line x1="4" y1="10" x2="16" y2="10" stroke="var(--card)" stroke-width="1.2"/>
      </svg>
      www.cellarhorizon4u.com
    </li>
  </ul>

  <ul class="social">
    <li><span class="social__tile" aria-hidden="true"></span>Chatterloop</li>
    <li><span class="social__tile" aria-hidden="true"></span>NestFinder</li>
  </ul>
</section>

</body>
</html>
```